Wordpress Design for my Consulting Company

We want a WordPress site created for our new business. We have created a mock-up of the content we want on the site at https://marcusdellow.example-sites.com/website-5

We are not attached to any of the pictures and just put stock stuff from wix's editor, which we don't have rights to use outside of wix.

We are NOT looking to just port this site to WordPress, we are looking for some creative ways to display the content in a more professional artistic sense.

I have included several logo files and a text file with the colors and Fonts used in the logo. We are not looking to change the logo or the colors used in the logo.

The Schedule appointment links to a page that embeds a bookingnest.example.com calendar. https://bookingnest.example.com/marcus-dellow/brightvale

The final website domain will be enterprisebrightvale.example

Enterprise brightvale is a consulting company that works directly with the business owners and leaders of small businesses between 50-200 employees. We help companies make sure they have the right technology to meet their strategic goals. We are the anti-"Computer Guy" and we focus on business outcomes NOT cool technology gadgets.

The final design should communicate business growth and success.

Target Market(s)

Business Owners of companies with 50-200 employees

Coding

Coded - Design and coding required

Number of Pages Required

1 page

Font styles to use
Serif
Other font styles liked:
• Trajan Pro Bold, Open Sans

Requirements
Must have
• Should focus on consulting rather than technology.
• Should show the customer as the hero and we are just their guide.
• Must use the logo provided and the colors and fonts in the text file provided. Any other colors and fonts must be complementary.
• The design should scale for all devices computer, iPad, or phone
Should not have
• Should not focus on technology, we are the anti-"Computer Guy" and we focus on business outcomes NOT cool technology gadgets.

```html
<!DOCTYPE html>
<html lang="en">
<head>
<meta charset="utf-8">
<title>Brightvale — Technology Advisors</title>
<link rel="stylesheet" href="https://fonts.googleapis.com/css2?family=Roboto:ital,wght@0,300;0,400;0,500;0,700;1,400&display=swap">
<style>
:root{
  --slate:#434f57;
  --slate-dark:#37424a;
  --orange:#c9774a;
  --orange-dark:#b8683d;
  --paper:#ffffff;
  --mist:#f1f2f3;
  --ink:#3b4349;
  --muted:#8b8f93;
  --line:#d8dbde;
}
*{box-sizing:border-box;margin:0;padding:0}
html,body{width:1200px;height:2528px;overflow:hidden;background:var(--paper)}
body{position:relative;font-family:"Roboto",Arial,sans-serif;color:var(--ink)}
.abs{position:absolute}

/* Hero */
.hero-photo{left:0;top:0;width:575px;height:602px;background:linear-gradient(180deg,#c9d3d8 0%,#9fb0b8 45%,#6d6a64 75%,#4a4641 100%)}
.hero-panel{left:575px;top:0;width:625px;height:602px;background:linear-gradient(160deg,#55626a 0%,var(--slate) 55%,#3c474e 100%)}
.brand{left:160px;top:34px;display:flex;align-items:center;gap:10px}
.brand-dot{width:40px;height:40px;border-radius:50%;background:var(--slate)}
.brand-name{font-family:"Roboto",Arial,sans-serif;font-weight:500;font-size:24px;color:var(--slate)}
.nav{left:704px;top:39px;display:flex;gap:28px;font-size:12.5px;color:#fff;letter-spacing:.3px}
.hero-box{left:489px;top:160px;width:548px;height:282px;border:2px solid #fff}
.hero-strip{left:489px;top:160px;width:68px;height:282px;background:#f4f1ee}
.hero-strip span{position:absolute;left:50%;top:50%;transform:translate(-50%,-50%) rotate(-90deg);font-size:36px;font-weight:700;color:var(--orange);letter-spacing:2px;white-space:nowrap}
.hero-kicker{left:603px;top:208px;font-size:22px;font-weight:300;color:#fff;letter-spacing:1px}
.hero-title{left:603px;top:235px;font-size:37px;font-weight:700;color:#fff;letter-spacing:.3px}
.hero-lead{left:605px;top:288px;width:360px;font-size:17px;font-weight:300;color:#fff;line-height:22px}
.btn-ghost{left:609px;top:357px;width:166px;height:36px;border:1.5px solid #fff;color:#fff;font-size:11.5px;display:flex;align-items:center;justify-content:center;letter-spacing:.4px}
.scroll-mouse{left:592px;top:557px;width:12px;height:20px;border:1.5px solid #fff;border-radius:7px}
.scroll-mouse::after{content:"";position:absolute;left:3.5px;top:4px;width:2px;height:5px;background:#fff;border-radius:1px}

/* About */
.guide-line{left:0;top:602px}
.about-label{left:84px;top:700px;width:80px;height:140px}
.about-label span{position:absolute;left:50%;top:50%;transform:translate(-50%,-50%) rotate(-90deg);font-size:32px;font-weight:300;color:var(--slate);letter-spacing:2px}
.about-rule{left:0;top:834px;width:140px;height:1px;background:var(--slate)}
.about-kicker{left:160px;top:668px;font-size:23px;font-weight:300;color:var(--ink)}
.about-title{left:160px;top:692px;font-size:36px;font-weight:700;color:var(--orange)}
.about-lead{left:160px;top:736px;width:475px;font-size:12.5px;font-style:italic;line-height:18px;color:var(--ink)}
.about-copy{left:160px;width:475px;font-size:11.5px;line-height:16.5px;color:var(--muted)}
.about-photo{left:662px;top:677px;width:375px;height:243px;background:linear-gradient(135deg,#c8ccd0 0%,#8d97a0 50%,#4d5862 100%);box-shadow:0 0 0 1px #e3e3e3}

/* Four steps */
.team-photo{left:0;top:977px;width:595px;height:455px;background:linear-gradient(180deg,#cfd6db 0%,#8c949a 55%,#3d4349 100%)}
.play{left:286px;top:1165px}
.steps-panel{left:595px;top:977px;width:605px;height:455px;background:linear-gradient(180deg,#f5f5f5,#ebebeb)}
.steps-mark{left:846px;top:1023px;width:60px;height:60px;border-radius:50%;background:var(--slate)}
.steps-title{left:595px;top:1099px;width:605px;text-align:center;font-size:26px;font-weight:700;color:var(--slate-dark)}
.steps-sub{left:595px;top:1135px;width:605px;text-align:center;font-size:19px;font-weight:300;color:var(--slate);line-height:23px}
.steps-intro{left:645px;top:1185px;width:505px;text-align:center;font-size:11px;line-height:16px;color:#a3a6a9}
.step{top:1244px;width:151px;height:188px;text-align:center;border-left:1px solid #e1e1e1;padding-top:32px}
.step svg{display:block;margin:0 auto}
.step h3{font-size:13px;font-weight:700;color:var(--slate-dark);margin-top:14px;letter-spacing:.3px}
.step p{font-size:10.5px;line-height:13.5px;color:var(--ink);margin:7px auto 0;width:118px}

/* Meeting */
.meeting-band{left:0;top:1432px;width:1200px;height:90px;background:linear-gradient(90deg,var(--orange-dark),var(--orange) 50%,var(--orange-dark))}
.meeting-band h2{text-align:center;line-height:90px;font-size:34px;font-weight:700;color:#fff;letter-spacing:.5px}
.day-head{left:0;top:1560px;width:1200px;text-align:center;font-size:24px;font-weight:700;color:var(--slate)}
.today{left:178px;top:1604px;font-size:14px;font-weight:700;color:var(--slate)}
.day{top:1636px;width:108px;height:108px;border-radius:50%;border:6px solid var(--orange);display:flex;align-items:center;justify-content:center}
.day-inner{width:88px;height:88px;border-radius:50%;border:1.5px solid var(--slate);display:flex;flex-direction:column;align-items:center;justify-content:center;line-height:16px}
.day-inner b{font-size:14px;color:var(--slate-dark)}
.day-inner small{font-size:12px;color:var(--slate)}
.card{top:1788px;width:276px;height:125px;background:var(--slate);color:#fff;text-align:center;display:flex;flex-direction:column;justify-content:center;font-size:17px;font-weight:500;line-height:20px;letter-spacing:.2px}
.arrow{top:1834px;width:32px;height:32px;border-radius:50%;background:#e6e7e8;display:flex;align-items:center;justify-content:center}

/* Contact strip */
.info-strip{left:0;top:1990px;width:1200px;height:79px;background:var(--mist)}
.info{top:2002px;display:flex;gap:12px;align-items:flex-start}
.info h4{font-size:12px;font-weight:500;color:var(--slate);margin-top:4px;letter-spacing:.3px}
.info p{font-size:14px;color:var(--slate-dark);margin-top:4px}
.info p.small{font-size:11px;line-height:14px}

/* Contact */
.contact-panel{left:0;top:2069px;width:607px;height:405px;background:var(--slate)}
.contact-label{left:84px;top:2110px;width:80px;height:170px}
.contact-label span{position:absolute;left:50%;top:50%;transform:translate(-50%,-50%) rotate(-90deg);font-size:32px;font-weight:300;color:#fff;letter-spacing:2px}
.contact-rule{left:0;top:2314px;width:135px;height:1px;background:#fff}
.field{left:160px;width:420px;height:36px;border:1px solid #6b767e;border-radius:3px;color:#c9ced2;font-size:11px;display:flex;align-items:center;gap:7px;padding-left:12px}
.field.message{align-items:flex-start;padding-top:12px;height:127px}
.btn-submit{left:160px;top:2405px;width:112px;height:34px;background:var(--orange);color:#fff;font-size:12.5px;font-weight:700;display:flex;align-items:center;justify-content:center;border-radius:2px}
.meeting-photo{left:607px;top:2069px;width:593px;height:405px;background:linear-gradient(135deg,#d9d6d0 0%,#a89c90 50%,#5a4b40 100%)}

/* Footer */
.footer{left:0;top:2474px;width:1200px;height:54px;background:var(--orange);color:#fff}
.copy{left:160px;top:20px;font-size:11px}
.social{right:160px;top:12px;display:flex;align-items:center;gap:8px;font-size:14px}
.social i{width:24px;height:24px;border:1.5px solid #fff;border-radius:50%;display:block}
</style>
</head>
<body>

<!-- Hero -->
<div class="abs hero-photo" role="img" aria-label="Businessman with briefcase standing at the end of a wooden walkway above a city"></div>
<div class="abs hero-panel"></div>
<div class="abs brand">
  <div class="brand-dot"></div>
  <div class="brand-name">Brightvale</div>
</div>
<nav class="abs nav"><span>HOME</span><span>ABOUT US</span><span>SERVICES</span><span>SCHEDULE APPOINTMENT</span></nav>
<div class="abs hero-box"></div>
<div class="abs hero-strip"><span>BRIGHTVALE</span></div>
<div class="abs hero-kicker">TECHNOLOGY ADVISORS</div>
<h1 class="abs hero-title">THAT "GET" BUSINESS.</h1>
<p class="abs hero-lead">We help you leverage technology to create a competitive advantage.</p>
<div class="abs btn-ghost">SCHEDULE APPOINTMENT</div>
<div class="abs scroll-mouse"></div>

<!-- About -->
<svg class="abs guide-line" width="400" height="90" viewBox="0 0 400 90">
  <path d="M37 0 V32 H388 V80" fill="none" stroke="#5a646b" stroke-width="1.2"/>
  <circle cx="388" cy="81" r="2.5" fill="#5a646b"/>
</svg>
<div class="abs about-label"><span>ABOUT</span></div>
<div class="abs about-rule"></div>
<div class="abs about-kicker">Helping associates to</div>
<h2 class="abs about-title">ACHIEVE SUCCESS</h2>
<p class="abs about-lead">Lorem Ipsum is simply dummy text of the printing and typesetting industry. Lorem Ipsum has been the industry's standard dummy...</p>
<p class="abs about-copy" style="top:780px">Lorem Ipsum is simply dummy text of the printing and typesetting industry. Lorem Ipsum has been the industry's standard dummy text ever since the 1500s, when an unknown printer took galley of type and scrambled it to make a type specimen book. It has survived not only five PageMaker including versions of Lorem Ipsum.</p>
<p class="abs about-copy" style="top:852px">Lorem Ipsum is simply dummy text of the printing and typesetting industry. Lorem Ipsum has been the industry's standard dummy text ever since the 1500s, when an unknown printer took galley of type and scrambled it to make a type specimen book. It has survived not only five PageMaker including versions of Lorem Ipsum.</p>
<div class="abs about-photo" role="img" aria-label="Two businessmen reviewing a tablet together at a desk"></div>

<!-- Four steps -->
<div class="abs team-photo" role="img" aria-label="Team of business professionals standing together in an office"></div>
<svg class="abs play" width="52" height="52" viewBox="0 0 52 52">
  <circle cx="26" cy="26" r="23" fill="none" stroke="#fff" stroke-width="3" opacity=".85"/>
  <path d="M20 15 L37 26 L20 37 Z" fill="#fff" opacity=".85"/>
</svg>
<div class="abs steps-panel"></div>
<div class="abs steps-mark"></div>
<h2 class="abs steps-title">THE FOUR STEPS</h2>
<p class="abs steps-sub">TO ALIGNING TECHNOLOGY TO YOUR BUSINESS<br>STRATEGY!</p>
<p class="abs steps-intro">Lorem Ipsum is simply dummy text of the printing and typesetting industry. Lorem Ipsum has galley of type and scrambled it to make a type specimen book. PageMaker including</p>

<div class="abs step" style="left:600px;border-left:none">
  <svg width="48" height="48" viewBox="0 0 48 48"><circle cx="20" cy="20" r="13" fill="none" stroke="#37424a" stroke-width="4"/><path d="M30 30 L43 43" stroke="#37424a" stroke-width="6" stroke-linecap="round"/></svg>
  <h3>DISCOVER</h3><p>Lorem Ipsum is simply printing and typesetting industry been...</p>
</div>
<div class="abs step" style="left:751px">
  <svg width="48" height="48" viewBox="0 0 48 48"><rect x="20" y="4" width="24" height="20" fill="none" stroke="#37424a" stroke-width="3"/><path d="M24 19 L30 13 L34 16 L40 9" fill="none" stroke="#37424a" stroke-width="2"/><circle cx="11" cy="10" r="5" fill="#37424a"/><path d="M5 18 H17 L22 24 L17 26 V44 H13 V32 H9 V44 H5 Z" fill="#37424a"/><path d="M32 24 V44 M26 44 H38" stroke="#37424a" stroke-width="2.5"/></svg>
  <h3>PRIORITIZE</h3><p>Lorem Ipsum is simply printing and typesetting industry been...</p>
</div>
<div class="abs step" style="left:902px">
  <svg width="48" height="48" viewBox="0 0 48 48"><g fill="#37424a"><circle cx="24" cy="24" r="14"/><rect x="20" y="4" width="8" height="40" rx="1"/><rect x="4" y="20" width="40" height="8" rx="1"/><rect x="20" y="4" width="8" height="40" rx="1" transform="rotate(45 24 24)"/><rect x="20" y="4" width="8" height="40" rx="1" transform="rotate(-45 24 24)"/></g><circle cx="24" cy="24" r="6" fill="#efefef"/></svg>
  <h3>IMPLEMENT</h3><p>Lorem Ipsum is simply printing and typesetting industry been...</p>
</div>
<div class="abs step" style="left:1053px">
  <svg width="48" height="48" viewBox="0 0 48 48"><path d="M24 8 a12 12 0 0 1 7 22 v5 h-14 v-5 a12 12 0 0 1 7 -22z" fill="none" stroke="#37424a" stroke-width="3"/><path d="M18 39 h12 M19 43 h10" stroke="#37424a" stroke-width="2.5"/><g stroke="#37424a" stroke-width="2.5" stroke-linecap="round"><path d="M24 1 v3 M8 8 l2 2 M40 8 l-2 2 M2 20 h3 M43 20 h3"/></g><circle cx="24" cy="20" r="4" fill="#37424a"/></svg>
  <h3>MAINTAIN</h3><p>Lorem Ipsum is simply printing and typesetting industry been...</p>
</div>

<!-- Meeting -->
<div class="abs meeting-band"><h2>BRIGHTVALE MEETING</h2></div>
<h2 class="abs day-head">SELECT A DAY</h2>
<div class="abs today">– TODAY –</div>
<div class="abs day" style="left:162px"><div class="day-inner"><b>MON</b><small>NOV 28</small></div></div>
<div class="abs day" style="left:288px"><div class="day-inner"><b>TUE</b><small>NOV 27</small></div></div>
<div class="abs day" style="left:414px"><div class="day-inner"><b>WED</b><small>NOV 28</small></div></div>
<div class="abs day" style="left:541px"><div class="day-inner"><b>THU</b><small>NOV 28</small></div></div>
<div class="abs day" style="left:671px"><div class="day-inner"><b>FRI</b><small>NOV 28</small></div></div>
<div class="abs day" style="left:799px"><div class="day-inner"><b>SAT</b><small>NOV 28</small></div></div>
<div class="abs day" style="left:928px"><div class="day-inner"><b>SUN</b><small>NOV 28</small></div></div>

<div class="abs arrow" style="left:95px"><svg width="10" height="12" viewBox="0 0 10 12"><path d="M7 1 L2 6 L7 11" fill="none" stroke="#8b8f93" stroke-width="2"/></svg></div>
<div class="abs card" style="left:162px">WE GET...<br>ELIMINATING BOTTLENECKS</div>
<div class="abs card" style="left:462px">WE GET...<br>STANDARDIZING CUSTOMER<br>EXPERIENCE</div>
<div class="abs card" style="left:762px">WE GET...<br>PREPARING FOR DISRUPTION</div>
<div class="abs arrow" style="left:1069px"><svg width="10" height="12" viewBox="0 0 10 12"><path d="M3 1 L8 6 L3 11" fill="none" stroke="#8b8f93" stroke-width="2"/></svg></div>

<!-- Contact strip -->
<div class="abs info-strip"></div>
<div class="abs info" style="left:160px">
  <svg width="52" height="46" viewBox="0 0 52 46"><g fill="none" stroke="#c9774a" stroke-width="2.2"><path d="M4 14 Q26 -2 48 14 L44 20 L36 16 L36 10 Q26 6 16 10 L16 16 L8 20 Z"/><path d="M14 20 L10 42 H42 L38 20 Z"/><circle cx="26" cy="31" r="6"/></g></svg>
  <div><h4>CALL TO US</h4><p>(555) 013-2847</p></div>
</div>
<div class="abs info" style="left:463px">
  <svg width="58" height="46" viewBox="0 0 58 46"><g fill="none" stroke="#c9774a" stroke-width="2.2"><rect x="3" y="8" width="52" height="34"/><path d="M3 8 L29 28 L55 8 M3 42 L22 23 M55 42 L36 23"/></g></svg>
  <div><h4>EMAIL</h4><p class="small" style="margin-top:8px">mdellow@enterprisebrightvale.example</p></div>
</div>
<div class="abs info" style="left:822px">
  <svg width="40" height="48" viewBox="0 0 40 48"><g fill="none" stroke="#c9774a" stroke-width="2.2"><path d="M20 46 C10 32 5 24 5 17 a15 15 0 0 1 30 0 c0 7 -5 15 -15 29z"/><circle cx="20" cy="17" r="6"/></g></svg>
  <div><h4>VISIT US</h4><p class="small">4120 Harlow Ridge Parkway,<br>Lakemont, TX 75001</p></div>
</div>

<!-- Contact -->
<div class="abs contact-panel"></div>
<div class="abs contact-label"><span>CONTACT</span></div>
<div class="abs contact-rule"></div>
<div class="abs field" style="top:2120px"><svg width="10" height="10" viewBox="0 0 10 10"><circle cx="5" cy="3" r="2.5" fill="#c9ced2"/><path d="M0 10 Q5 3 10 10Z" fill="#c9ced2"/></svg>Name:</div>
<div class="abs field" style="top:2169px"><svg width="11" height="9" viewBox="0 0 11 9"><rect width="11" height="9" fill="#c9ced2"/><path d="M0 0 L5.5 5 L11 0" fill="none" stroke="#434f57"/></svg>Email:</div>
<div class="abs field" style="top:2219px"><svg width="7" height="11" viewBox="0 0 7 11"><rect x=".5" y=".5" width="6" height="10" rx="1" fill="none" stroke="#c9ced2"/></svg>Phone Number:</div>
<div class="abs field message" style="top:2268px"><svg width="12" height="10" viewBox="0 0 12 10"><ellipse cx="6" cy="4" rx="6" ry="4" fill="#c9ced2"/><path d="M2 7 L1 10 L5 7.5Z" fill="#c9ced2"/></svg>Message:</div>
<div class="abs btn-submit">SUBMIT NOW</div>
<div class="abs meeting-photo" role="img" aria-label="Three colleagues in a meeting at a conference table reviewing documents"></div>

<!-- Footer -->
<footer class="abs footer">
  <div class="abs copy">Copyright 2018 brightvale.example</div>
  <div class="abs social">Connect with us: <i></i><i></i><i></i></div>
</footer>

</body>
</html>
```